Website update for Harborline Ledger & Payroll Services

Our website needs updating
www.harborlineledgerservices.com
Here are some of our latest print pieces to use as a guide?
I have also attached our graphic identity guide which includes the Pantone colors

Target Market(s)

Insurance Agencies

Industry/Entity Type

Accounting

Number of Pages Required

5+ page

```html
<!DOCTYPE html>
<html lang="en">
<head>
<meta charset="utf-8">
<title>Harborline Ledger & Payroll Services</title>
<link href="https://fonts.googleapis.com/css2?family=Open+Sans:wght@400;600;700&family=Raleway:wght@400;600;700&display=swap" rel="stylesheet">
<style>
:root{
  --teal:#17a99b;
  --teal-dark:#10897d;
  --navy:#1d3447;
  --ink:#333d44;
  --muted:#7b868d;
  --paper:#ffffff;
  --cream:#f3f1ec;
  --grey:#e9ecee;
  --night:#1d2328;
}
*{box-sizing:border-box;margin:0;padding:0}
html,body{width:1200px;height:2736px;overflow:hidden}
body{font-family:"Open Sans",Arial,sans-serif;color:var(--ink);background:var(--paper);position:relative}
.site{position:relative;width:1200px;height:2736px}

/* header */
.topbar{position:absolute;top:0;left:0;width:1200px;height:232px;background:var(--cream)}
.contact-call,.contact-mail{position:absolute;top:40px;display:flex;align-items:center;gap:12px;font-size:15px;color:var(--navy)}
.contact-call{left:90px}
.contact-mail{right:90px;text-align:right}
.contact-call small,.contact-mail small{display:block;font-size:12px;color:var(--teal);font-weight:600}
.dot-icon{width:34px;height:34px;border-radius:50%;background:var(--teal);display:flex;align-items:center;justify-content:center}
.brand{position:absolute;top:34px;left:0;width:1200px;display:flex;justify-content:center;align-items:center;gap:14px}
.brand-mark{width:58px;height:58px;background:var(--teal)}
.brand-name{font-family:"Raleway",sans-serif;font-weight:700;font-size:30px;color:var(--navy);line-height:1.05;width:330px}
.tagline{position:absolute;top:132px;width:1200px;text-align:center;font-family:"Raleway",sans-serif;font-size:21px;font-weight:600;color:var(--navy)}
.tagline b{color:var(--teal)}
.nav{position:absolute;top:184px;left:120px;width:960px;height:48px;background:var(--paper);display:flex;border-top:1px solid var(--grey)}
.nav a{flex:1;text-align:center;line-height:48px;font-size:12px;font-weight:600;color:var(--navy);text-decoration:none;letter-spacing:.5px}
.nav a.active{background:var(--teal);color:#fff}

/* hero */
.hero{position:absolute;top:232px;left:0;width:1200px;height:628px;background:linear-gradient(100deg,#1c2a33 0%,#35464f 45%,#7d8b90 75%,#c3b89f 100%)}
.hero-copy{position:absolute;left:48px;top:180px;width:760px;color:#fff}
.hero-copy h1{font-family:"Raleway",sans-serif;font-size:40px;font-weight:700;color:var(--teal);line-height:1.15;text-transform:uppercase;margin-bottom:28px}
.hero-copy ul{list-style:none;font-size:19px;line-height:1.45}
.hero-copy li{position:relative;padding-left:28px;margin-bottom:16px}
.hero-copy li::before{content:"";position:absolute;left:4px;top:10px;width:9px;height:9px;border-radius:50%;background:#fff}
.btn{display:inline-block;background:var(--teal);color:#fff;font-size:13px;font-weight:700;padding:12px 28px;letter-spacing:.5px}

/* welcome */
.welcome{position:absolute;top:860px;left:0;width:1200px;height:340px;text-align:center;padding-top:80px}
.section-title{font-family:"Raleway",sans-serif;font-size:42px;font-weight:700;color:var(--navy)}
.section-title span{color:var(--teal)}
.rule{width:100px;height:3px;background:var(--teal);margin:12px auto 22px}
.welcome p{width:980px;margin:0 auto 30px;font-size:13px;line-height:1.6;color:var(--muted)}

/* services */
.services{position:absolute;top:1200px;left:0;width:1200px;height:380px;background:var(--teal);text-align:center;padding-top:60px;color:#fff}
.services .section-title{color:#fff}
.services .rule{background:#fff}
.services p{width:1040px;margin:0 auto 40px;font-size:13px;line-height:1.6}
.cards{display:flex;justify-content:center;gap:24px}
.card{width:240px;height:130px;background:#fff;color:var(--navy);font-weight:700;font-size:15px;display:flex;flex-direction:column;align-items:center;justify-content:center;gap:18px}
.card-icon{width:56px;height:56px;border-radius:50%;background:var(--teal);display:flex;align-items:center;justify-content:center}

/* team */
.team{position:absolute;top:1580px;left:0;width:1200px;height:220px;text-align:center;padding-top:60px;font-family:"Raleway",sans-serif}
.team h2{font-size:34px;font-weight:700;color:var(--navy)}
.team h3{font-size:32px;font-weight:600;color:var(--teal)}

.feature{position:absolute;left:0;width:1200px;height:270px}
.feature.one{top:1800px}
.feature.two{top:2080px}
.feature-photo{position:absolute;top:0;width:520px;height:270px}
.feature.one .feature-photo{left:0;background:linear-gradient(120deg,#0f1418,#2b3b44 60%,#1a2429)}
.feature.two .feature-photo{right:0;background:linear-gradient(120deg,#3e4a50,#1d252a)}
.feature-photo span{position:absolute;font-family:"Raleway",sans-serif;font-weight:700;font-size:26px;color:var(--teal);line-height:1.2}
.feature.one .feature-photo span{left:50px;top:100px;width:440px;text-align:center}
.feature.two .feature-photo span{left:240px;top:150px;font-size:28px}
.ticks{position:absolute;top:50px;list-style:none;font-size:15px;line-height:1.5;color:var(--ink)}
.feature.one .ticks{left:600px;width:520px}
.feature.two .ticks{left:120px;width:520px}
.ticks li{display:flex;gap:14px;margin-bottom:26px}
.ticks svg{flex:none;margin-top:4px}

/* footer */
.footer{position:absolute;top:2400px;left:0;width:1200px;height:300px;background:var(--teal);color:#fff;display:flex}
.footer-col{padding:40px 40px 0}
.footer-col h4{font-family:"Raleway",sans-serif;font-size:17px;font-weight:700;margin-bottom:8px}
.footer-col .line{width:50px;height:2px;background:#fff;margin-bottom:18px}
.footer-col p{font-size:13px;line-height:1.6}
.about{width:400px}
.news{width:420px;background:var(--grey);color:var(--navy)}
.news .line{background:var(--teal)}
.news input{display:block;width:320px;height:36px;border:1px solid #cfd5d8;margin:16px 0 10px;background:#fff}
.news .btn{padding:10px 110px;background:#9aa4a9}
.location{width:380px}
.location p{display:flex;gap:10px;margin-bottom:8px}
.bottom{position:absolute;top:2700px;left:0;width:1200px;height:36px;background:var(--night);color:#b8c0c4;font-size:12px;text-align:center;line-height:36px}
.social{position:absolute;right:40px;top:8px;display:flex;gap:8px}
.social i{width:20px;height:20px;background:var(--teal);display:block}
</style>
</head>
<body>
<div class="site">
  <header class="topbar">
    <div class="contact-call"><span class="dot-icon"><svg width="16" height="16" viewBox="0 0 24 24"><path d="M6.6 10.8a15 15 0 0 0 6.6 6.6l2.2-2.2c.3-.3.7-.4 1-.2 1.1.4 2.3.6 3.6.6.6 0 1 .4 1 1V20c0 .6-.4 1-1 1A17 17 0 0 1 3 4c0-.6.4-1 1-1h3.5c.6 0 1 .4 1 1 0 1.3.2 2.5.6 3.6.1.3 0 .7-.2 1z" fill="#fff"/></svg></span><div><small>CALL US</small>1 415 555 0182</div></div>
    <div class="brand"><span class="brand-mark"></span><span class="brand-name">Harborline Ledger &amp; Payroll Services</span></div>
    <div class="contact-mail"><div><small>EMAIL US</small>info@harborlineledgerservices.com</div><span class="dot-icon"><svg width="16" height="16" viewBox="0 0 24 24"><path d="M3 5h18v14H3z" fill="none" stroke="#fff" stroke-width="2"/><path d="M3 6l9 7 9-7" fill="none" stroke="#fff" stroke-width="2"/></svg></span></div>
    <p class="tagline">Specialists in providing accounting support <b>services to Independent Insurance Agencies</b></p>
    <nav class="nav">
      <a class="active">HOME</a><a>ABOUT US</a><a>COMPANY</a><a>OUR SERVICES</a><a>HOW IT WORKS</a><a>RESOURCES</a><a>CONTACT US</a><a>BLOG</a>
    </nav>
  </header>

  <section class="hero" role="img" aria-label="Photo of a desk with a small model house, calculator and paperwork">
    <div class="hero-copy">
      <h1>Need help with your insurance agency's accounting and bookkeeping?</h1>
      <ul>
        <li>Put our team of insurance agency bookkeeping professionals to work for you.</li>
        <li>Have a cross-trained team working in a controlled office environment in Northwest Connecticut at your service.</li>
        <li>Be presented with monthly financial statements reviewed by an accountant with 35 years' experience working in insurance agencies.</li>
      </ul>
      <span class="btn" style="margin-top:14px">READ MORE</span>
    </div>
  </section>

  <section class="welcome">
    <h2 class="section-title">WELCOME TO <span>Harborline</span></h2>
    <div class="rule"></div>
    <p>We keep the books for independent insurance agencies so owners can focus on clients and growth. Our team records commissions, reconciles bank accounts, posts customer payments and pays operating invoices on schedule. Each month you receive clear financial statements, reviewed by an experienced accountant, that show exactly where your agency stands and what needs attention next.</p>
    <span class="btn">READ MORE</span>
  </section>

  <section class="services">
    <h2 class="section-title">OUR <span style="color:#fff;font-weight:400">SERVICE</span></h2>
    <div class="rule"></div>
    <p>From daily postings to monthly close, our services cover the routine work that keeps an agency's finances accurate. We tailor every engagement to your systems, carriers and reporting needs, and we stay in close contact so nothing slips between statements.</p>
    <div class="cards">
      <div class="card"><span class="card-icon"><svg width="26" height="26" viewBox="0 0 24 24"><rect x="5" y="3" width="14" height="18" fill="none" stroke="#fff" stroke-width="2"/><path d="M8 7h8M8 11h2M12 11h2M8 15h2M12 15h2" stroke="#fff" stroke-width="2"/></svg></span>Direct bill commission tracked</div>
      <div class="card"><span class="card-icon"><svg width="26" height="26" viewBox="0 0 24 24"><rect x="3" y="6" width="18" height="12" fill="none" stroke="#fff" stroke-width="2"/><circle cx="12" cy="12" r="2.5" fill="#fff"/></svg></span>Customer payments posted</div>
      <div class="card"><span class="card-icon"><svg width="26" height="26" viewBox="0 0 24 24"><circle cx="9" cy="10" r="4" fill="none" stroke="#fff" stroke-width="2"/><circle cx="16" cy="16" r="3" fill="none" stroke="#fff" stroke-width="2"/></svg></span>Operating invoices paid</div>
      <div class="card"><span class="card-icon"><svg width="26" height="26" viewBox="0 0 24 24"><circle cx="12" cy="8" r="4" fill="#fff"/><path d="M4 21c1-5 15-5 16 0" fill="#fff"/></svg></span>Bank accounts reconciled</div>
    </div>
  </section>

  <section class="team">
    <h2>Experienced Team of Insurance Agency Bookkeeping</h2>
    <h3>Professionals Maintaining Your Books</h3>
  </section>

  <section class="feature one">
    <div class="feature-photo" role="img" aria-label="Dark photo of business hands over glowing financial graphics"><span>Affordable, Professional Services For Less Than the Cost of an In-House Bookkeeper</span></div>
    <ul class="ticks">
      <li><svg width="16" height="16" viewBox="0 0 16 16"><path d="M2 8l4 4 8-9" fill="none" stroke="#17a99b" stroke-width="2.5"/></svg>Pay for what you need, when you need it</li>
      <li><svg width="16" height="16" viewBox="0 0 16 16"><path d="M2 8l4 4 8-9" fill="none" stroke="#17a99b" stroke-width="2.5"/></svg>No more year-end headaches – eliminate the need for re-work</li>
      <li><svg width="16" height="16" viewBox="0 0 16 16"><path d="M2 8l4 4 8-9" fill="none" stroke="#17a99b" stroke-width="2.5"/></svg>Ongoing updates of financial records and reports</li>
    </ul>
  </section>

  <section class="feature two">
    <ul class="ticks">
      <li><svg width="16" height="16" viewBox="0 0 16 16"><path d="M2 8l4 4 8-9" fill="none" stroke="#17a99b" stroke-width="2.5"/></svg>Services from routine bookkeeping to financial analysis</li>
      <li><svg width="16" height="16" viewBox="0 0 16 16"><path d="M2 8l4 4 8-9" fill="none" stroke="#17a99b" stroke-width="2.5"/></svg>Specializing in agency &amp; bookkeeping software: LedgerDesk, AgencyBase, PolicyRoll, CoverTrack, QuoteBridge</li>
      <li><svg width="16" height="16" viewBox="0 0 16 16"><path d="M2 8l4 4 8-9" fill="none" stroke="#17a99b" stroke-width="2.5"/></svg>Train and educate bookkeepers, managers, owners</li>
    </ul>
    <div class="feature-photo" role="img" aria-label="Grey photo of a wall with printed words about climate and business"><span>Capabilities</span></div>
  </section>

  <footer class="footer">
    <div class="footer-col about">
      <h4>ABOUT US</h4><div class="line"></div>
      <p>Harborline supports independent insurance agencies with dependable bookkeeping, payroll and monthly reporting. Our staff understands carrier statements, commission schedules and agency management systems, so your records stay accurate and ready for review at any time.</p>
      <span class="btn" style="background:var(--teal-dark);margin-top:20px">READ MORE</span>
    </div>
    <div class="footer-col news">
      <h4>NEWSLETTER SIGNUP</h4><div class="line"></div>
      <p>Subscribe to our newsletter to hear our latest updates and offers, plus practical tips on agency finances sent to you each month.</p>
      <input type="text" aria-label="Email address">
      <span class="btn">SUBSCRIBE</span>
    </div>
    <div class="footer-col location">
      <h4>LOCATION</h4><div class="line"></div>
      <p>◉ <span>Harborline Ledger &amp; Payroll Services<br>218 Millbrook Road<br>Torrington, CT 06790</span></p>
      <p>☏ <span>Office: 415-555-0182</span></p>
      <p>☏ <span>Fax: 415-555-0199</span></p>
      <p>✉ <span>info@harborlineledgerservices.com</span></p>
    </div>
  </footer>
  <div class="bottom">Copyright 2016 Harborline Ledger &amp; Payroll Services. All rights reserved.
    <div class="social"><i></i><i></i><i></i></div>
  </div>
</div>
</body>
</html>
```